facelift of our car wrap design - for Varno Klido L2

We would like to give our vehicles a facelift. Attached is our current advertising material.
Must-have: The paintwork of our vehicles is and will remain yellow. I would prefer to use the newer company logo, without the coloured bars, as shown in the attachment.
You can find further inspiration at www.plimtaaab.ch.

it should be a classic new design

• some advertising keywords

```html
<!DOCTYPE html>
<html lang="de">
<head>
<meta charset="utf-8">
<title>Plimtaaab – Fahrzeugbeschriftung Varno Klido L2</title>
<link rel="stylesheet" href="https://fonts.googleapis.com/css2?family=Barlow:wght@500;700;800&family=Barlow+Condensed:wght@600&display=swap">
<style>
  :root{
    --paint:#f7d417;
    --panel:#b79b0a;
    --ink:#111111;
    --trim:#3a3a3c;
    --glass:#e4e6e8;
    --glass-edge:#9ea3a8;
    --lamp:#c9272b;
    --tyre:#1c1c1c;
    --rim:#bfc3c7;
    --page:#ffffff;
  }
  html,body{margin:0;padding:0;overflow:hidden;background:var(--page);}
  .sheet{display:block;width:1200px;height:623px;}
  .body-paint{fill:var(--paint);stroke:var(--trim);stroke-width:1.5;}
  .panel-line{fill:none;stroke:var(--panel);stroke-width:1.2;}
  .glass{fill:var(--glass);stroke:var(--glass-edge);stroke-width:1.5;}
  .trim{fill:var(--trim);}
  .tyre{fill:var(--tyre);}
  .rim{fill:var(--rim);stroke:#7d8186;stroke-width:2;}
  .lamp{fill:var(--lamp);}
  .plate{fill:#ffffff;stroke:#888888;}
  .headlamp{fill:#f4f4f4;stroke:#777777;}
  .brand{font-family:"Barlow",sans-serif;font-weight:800;fill:var(--ink);letter-spacing:1px;}
  .tagline{font-family:"Barlow",sans-serif;font-weight:500;fill:var(--ink);letter-spacing:1px;}
  .web{font-family:"Barlow",sans-serif;font-weight:700;fill:var(--ink);}
  .keywords{font-family:"Barlow Condensed",sans-serif;font-weight:600;fill:var(--ink);}
  .icon{fill:none;stroke:var(--ink);stroke-width:2.2;stroke-linecap:round;stroke-linejoin:round;}
</style>
</head>
<body>
<svg class="sheet" viewBox="0 0 1200 623" xmlns="http://www.w3.org/2000/svg">
  <defs>
    <symbol id="icon-tap" viewBox="0 0 40 40">
      <path class="icon" d="M4 34h32M8 34V26h20v8M10 26V14h14M24 14v-4h-6M30 14v8"/>
    </symbol>
    <symbol id="icon-radiator" viewBox="0 0 40 40">
      <path class="icon" d="M6 8h5v26H6zM13 8h5v26h-5zM20 8h5v26h-5zM27 8h5v26h-5zM4 12h30M4 30h30"/>
    </symbol>
    <symbol id="icon-roof" viewBox="0 0 40 40">
      <path class="icon" d="M2 34L20 8h18L22 34zM10 30l14-18"/>
    </symbol>
    <symbol id="icon-service" viewBox="0 0 40 40">
      <path class="icon" d="M8 30l14-14M22 16a6 6 0 1 0 6-8l-4 4 4 4 4-4M26 26l8 8M18 22l-8-10"/>
    </symbol>
    <symbol id="icon-tools" viewBox="0 0 40 40">
      <path class="icon" d="M8 8l24 24M32 8L8 32M6 6l4-2 4 4-2 4zM30 34l4-4"/>
    </symbol>

    <g id="van-side">
      <path class="body-paint" d="M66 60Q66 38 95 36L540 38Q562 40 582 56L662 122Q702 136 742 150Q802 166 812 200L815 250Q812 262 790 262L752 262A62 62 0 0 0 628 262L262 262A62 62 0 0 0 138 262L66 262Q58 262 58 240Z"/>
      <path class="glass" d="M410 46L536 46Q552 48 566 60L630 120L410 120Z"/>
      <path class="panel-line" d="M250 40V246M400 40V246M120 118H560"/>
      <rect class="trim" x="58" y="222" width="76" height="40"/>
      <rect class="trim" x="262" y="248" width="366" height="9" rx="3"/>
      <rect class="trim" x="756" y="200" width="59" height="62" rx="8"/>
      <rect class="lamp" x="62" y="118" width="14" height="48" rx="3"/>
      <circle class="tyre" cx="200" cy="266" r="46"/><circle class="rim" cx="200" cy="266" r="26"/>
      <circle class="tyre" cx="690" cy="266" r="46"/><circle class="rim" cx="690" cy="266" r="26"/>
    </g>
  </defs>

  <!-- Side view -->
  <g class="view view-side">
    <g role="img" aria-label="Varno Klido L2 Seitenansicht, gelb lackiert">
      <use href="#van-side"/>
    </g>
    <text class="brand" x="156" y="100" font-size="36">PLIMTAAAB</text>
    <text class="tagline" x="156" y="123" font-size="17">HAUSTECHNIK + BAUSPENGLEREI</text>
    <use href="#icon-tap" x="320" y="176" width="38" height="38"/>
    <use href="#icon-radiator" x="376" y="176" width="38" height="38"/>
    <use href="#icon-roof" x="436" y="176" width="46" height="38"/>
    <use href="#icon-service" x="506" y="176" width="38" height="38"/>
    <use href="#icon-tools" x="560" y="176" width="38" height="38"/>
    <text class="keywords" x="308" y="234" font-size="13.5" textLength="292" lengthAdjust="spacingAndGlyphs">Sanitär, Heizung, Bauspenglerei, Service, Wartung, Unterhalt</text>
  </g>

  <!-- Side view with web address -->
  <g class="view view-side-web" transform="translate(0 297)">
    <g role="img" aria-label="Varno Klido L2 Seitenansicht mit Webadresse, gelb lackiert">
      <use href="#van-side"/>
    </g>
    <text class="brand" x="156" y="100" font-size="36">PLIMTAAAB</text>
    <text class="tagline" x="156" y="123" font-size="17">HAUSTECHNIK + BAUSPENGLEREI</text>
    <text class="web" x="156" y="150" font-size="13">www.plimtaaab.ch</text>
    <use href="#icon-tap" x="320" y="176" width="38" height="38"/>
    <use href="#icon-radiator" x="376" y="176" width="38" height="38"/>
    <use href="#icon-roof" x="436" y="176" width="46" height="38"/>
    <use href="#icon-service" x="506" y="176" width="38" height="38"/>
    <use href="#icon-tools" x="560" y="176" width="38" height="38"/>
    <text class="keywords" x="308" y="234" font-size="13.5" textLength="292" lengthAdjust="spacingAndGlyphs">Sanitär, Heizung, Bauspenglerei, Service, Wartung, Unterhalt</text>
  </g>

  <!-- Rear view -->
  <g class="view view-rear">
    <g role="img" aria-label="Varno Klido L2 Heckansicht, gelb lackiert">
      <rect class="trim" x="867" y="108" width="22" height="30" rx="4"/>
      <rect class="trim" x="1150" y="108" width="22" height="30" rx="4"/>
      <path class="body-paint" d="M910 30Q1020 20 1130 30Q1148 34 1148 60L1150 250L890 250L892 60Q892 34 910 30Z"/>
      <rect class="panel-line" x="928" y="52" width="184" height="76" rx="8"/>
      <rect class="lamp" x="893" y="140" width="24" height="60" rx="4"/>
      <rect class="lamp" x="1124" y="140" width="24" height="60" rx="4"/>
      <rect class="plate" x="934" y="196" width="76" height="20" rx="3"/>
      <path class="panel-line" d="M1020 30V52M1020 128V250"/>
      <rect class="trim" x="888" y="248" width="264" height="34" rx="6"/>
      <rect class="tyre" x="896" y="280" width="36" height="34" rx="5"/>
      <rect class="tyre" x="1108" y="280" width="36" height="34" rx="5"/>
    </g>
    <text class="brand" x="936" y="96" font-size="20">PLIMTAAAB</text>
    <text class="tagline" x="936" y="111" font-size="9.5">HAUSTECHNIK + BAUSPENGLEREI</text>
    <g class="keywords" font-size="10">
      <use href="#icon-tap" x="1032" y="134" width="12" height="12"/><text x="1050" y="144">Sanitär</text>
      <use href="#icon-radiator" x="1032" y="149" width="12" height="12"/><text x="1050" y="159">Heizung</text>
      <use href="#icon-roof" x="1032" y="164" width="12" height="12"/><text x="1050" y="174">Bauspenglerei</text>
      <use href="#icon-service" x="1032" y="179" width="12" height="12"/><text x="1050" y="189">Service</text>
      <use href="#icon-tools" x="1032" y="194" width="12" height="12"/><text x="1050" y="204">Wartung</text>
      <use href="#icon-tools" x="1032" y="209" width="12" height="12"/><text x="1050" y="219">Unterhalt</text>
    </g>
    <text class="web" x="963" y="241" font-size="13">www.plimtaaab.ch</text>
  </g>

  <!-- Front view -->
  <g class="view view-front">
    <g role="img" aria-label="Varno Klido L2 Frontansicht, gelb lackiert">
      <rect class="trim" x="876" y="410" width="24" height="32" rx="5"/>
      <rect class="trim" x="1148" y="410" width="24" height="32" rx="5"/>
      <path class="body-paint" d="M920 348Q1024 336 1128 348Q1146 352 1150 380L1158 540L890 540L898 380Q902 352 920 348Z"/>
      <path class="glass" d="M922 356Q1024 346 1126 356L1136 430Q1024 438 912 430Z"/>
      <ellipse class="headlamp" cx="928" cy="474" rx="26" ry="14"/>
      <ellipse class="headlamp" cx="1120" cy="474" rx="26" ry="14"/>
      <rect class="trim" x="972" y="470" width="104" height="22" rx="6"/>
      <rect class="trim" x="890" y="520" width="268" height="60" rx="8"/>
      <rect class="plate" x="986" y="534" width="76" height="18" rx="3"/>
      <rect class="tyre" x="898" y="578" width="36" height="26" rx="5"/>
      <rect class="tyre" x="1114" y="578" width="36" height="26" rx="5"/>
    </g>
    <text class="brand" x="968" y="454" font-size="17">PLIMTAAAB</text>
    <text class="tagline" x="968" y="467" font-size="8.5">HAUSTECHNIK + BAUSPENGLEREI</text>
  </g>
</svg>
</body>
</html>
```